Professional New Resume for personal/ company

Specialist in construction law, disputes and quantity surveying. Looking for a new fresh CV to appeal to the middle east (UAE) market.

Target Market(s)

employers, clients, lawyers, expert witnesses

Industry/Entity Type

Construction law, quantity surveying, dispute resolution.

```html
<!DOCTYPE html>
<html lang="en">
<head>
<meta charset="utf-8">
<title>Calum J Moray – Resume</title>
<link href="https://fonts.googleapis.com/css2?family=Tinos:wght@400;700&display=swap" rel="stylesheet">
<style>
:root{
  --backdrop:#5b96a0;
  --teal:#276b7a;
  --band:#e6e6e6;
  --paper:#ffffff;
  --ink-strong:#3f4648;
  --ink:#666c6e;
  --white:#ffffff;
}
*{margin:0;padding:0;box-sizing:border-box}
html,body{width:1200px;height:900px;overflow:hidden;background:var(--backdrop)}
body{font-family:"Tinos","Times New Roman",serif;position:relative}
.page{position:absolute;top:103px;width:493px;height:696px;background:var(--paper);overflow:hidden}
.page--one{left:80px}
.page--two{left:626px}
.header{position:absolute;left:0;top:0;width:100%;height:108px;background:var(--teal)}
.portrait{position:absolute;left:59px;top:5px;width:98px;height:98px;border-radius:50%;border:2px solid var(--white);
  background:radial-gradient(circle at 50% 35%,#d9b9a3 0 18%,#e9e4df 19% 40%,#2f3136 41% 100%)}
.name{position:absolute;left:169px;top:37px;color:var(--white);font-weight:700;font-size:23.5px;letter-spacing:.3px}
.tagline{position:absolute;left:0;top:108px;width:100%;height:26px;background:var(--band);color:#555b5d;font-weight:700;
  font-size:11.3px;text-align:center;line-height:26px;letter-spacing:.1px}
.pill{position:absolute;height:20px;border-radius:10px;background:var(--teal);color:var(--white);font-weight:700;
  font-size:11px;letter-spacing:.6px;text-align:center;line-height:20px}
.col-left{left:17px;width:182px}
.col-right{left:233px;width:240px}
.text{position:absolute;font-size:7.6px;line-height:11.6px;color:var(--ink)}
.contact-row{position:absolute;left:17px;font-size:7.6px;color:var(--ink);line-height:11px}
.contact-row svg{position:absolute;left:0;top:1px}
.contact-row span{position:absolute;left:16px;white-space:nowrap}
.item{position:absolute;font-size:7.6px;line-height:11.6px;color:var(--ink)}
.item::before{content:"";position:absolute;left:-10px;top:3.5px;width:4.5px;height:4.5px;border-radius:50%;background:var(--teal)}
.item b{color:var(--ink-strong);font-weight:700}
.justify{text-align:justify}
.date{position:absolute;font-size:7.6px;font-weight:700;color:var(--ink-strong);text-align:right;width:60px}
</style>
</head>
<body>

<section class="page page--one">
  <div class="header">
    <div class="portrait" role="img" aria-label="Portrait photo of the consultant in a dark pinstripe suit"></div>
    <h1 class="name">CALUM J MORAY</h1>
  </div>
  <p class="tagline">Construction Law, Disputes and Quantity Surveying Specialist</p>

  <h2 class="pill col-left" style="top:158px">CONTACT</h2>
  <div class="contact-row" style="top:190px">
    <svg width="9" height="9" viewBox="0 0 10 10"><path d="M2 1l2 2-1 1.3c.6 1.3 1.5 2.2 2.7 2.7L7 6l2 2-1.3 1.3C4.5 9 1 5.5.7 2.3z" fill="none" stroke="#276b7a" stroke-width=".8"/></svg>
    <span>+44 (0)7000 123 456</span></div>
  <div class="contact-row" style="top:206px">
    <svg width="9" height="9" viewBox="0 0 10 10"><rect x=".5" y="2" width="9" height="6" fill="none" stroke="#276b7a" stroke-width=".8"/><path d="M.5 2l4.5 3.5L9.5 2" fill="none" stroke="#276b7a" stroke-width=".8"/></svg>
    <span>calum@cjmqs.example</span></div>
  <div class="contact-row" style="top:222px">
    <svg width="9" height="11" viewBox="0 0 10 12"><path d="M5 11C2 7 1.5 5.5 1.5 4.5a3.5 3.5 0 017 0C8.5 5.5 8 7 5 11z" fill="none" stroke="#276b7a" stroke-width=".8"/><circle cx="5" cy="4.5" r="1.3" fill="none" stroke="#276b7a" stroke-width=".8"/></svg>
    <span>2nd Floor, 15 Harrow Crescent, Glasgow,</span></div>
  <div class="contact-row" style="top:238px"><span style="left:18px">Scotland, United Kingdom, G1 0AA</span></div>

  <h2 class="pill col-left" style="top:271px">OVERWIEW</h2>
  <p class="text justify" style="left:17px;top:301px;width:182px">Adjudicator, Chartered Quantity Surveyor and Chartered Construction Manager with experience in Private Practice, Development and Main Contracting industry. Claims, contract and dispute resolution (adjudication) services (as adjudicator or party representative) provided in Scotland, England and Wales. nibh euismod tincidunt ut</p>

  <h2 class="pill col-left" style="top:408px">QUALIFICATION</h2>
  <p class="item" style="left:31px;top:438px">BSc (Hons) Quantity Surveying<br>Clydebank Technical University</p>
  <p class="item" style="left:31px;top:463px">LL.M Masters of Law (With Merit)<br>University of Lowmoor</p>
  <p class="item" style="left:31px;top:488px">Diploma in Adjudication (IDArb)</p>

  <h2 class="pill col-left" style="top:522px">MEMBERSHIP</h2>
  <p class="item" style="left:31px;top:552px;width:135px">Fellow of The Institute of Dispute Arbitrators</p>
  <p class="item" style="left:31px;top:576px;width:135px">Fellow of The Royal Institute of Building Surveyors</p>
  <p class="item" style="left:31px;top:600px;width:135px">Member of The Institute of Civil Engineering Estimators</p>
  <p class="item" style="left:31px;top:625px;width:135px">Member of The Institute of Construction Managers</p>
  <p class="item" style="left:31px;top:649px;width:145px">Adjudicator &amp; Panel Member – NAP (National Adjudicators Panel)</p>

  <h2 class="pill col-right" style="top:158px">EXPERIENCE</h2>
  <p class="item" style="left:243px;top:187px;width:230px"><b>Tribunal secretary to assist the Arbitral Tribunal</b><br>Parties to an International Arbitration<br>(December 2020 to Current)</p>
  <p class="item" style="left:243px;top:228px;width:200px"><b>Adjudicator</b><br>Adjudicator in Construction Disputes, nominated by National Adjudicators Panel.<br>(December 2021 to Current)</p>
  <p class="item" style="left:243px;top:280px;width:230px"><b>Representative for Referring Party</b><br>Referring Party (Contractor)<br>December 2020</p>
  <p class="item" style="left:243px;top:321px;width:230px"><b>Representative for Referring Party</b><br>Referring Party (Subcontractor)<br>January 2019</p>
  <p class="item justify" style="left:243px;top:364px;width:230px"><b>Conclude and implement compensation event quotations under SCF3/4 contracts. Commercial management services, procurement advice, dispute avoidance.</b><br>Granton plc (consulting for Veltrex International)<br>February 2019 to Current</p>
  <p class="item" style="left:243px;top:432px;width:215px"><b>Review of Memorandum of Understanding, Nimbus standard services contract, alignment of contracts.</b><br>Consulting for Veltrex International<br>January to February 2019</p>
  <p class="item justify" style="left:243px;top:487px;width:230px"><b>Contract and commercial management of BCC D&amp;B contract; dispute avoidance; claim preparation for loss and/ or expense; legal opinion instructed from leading QC of 12 Aldgate Chambers regarding liquidated damages clause within contract.</b><br>Castelline<br>2018</p>
  <p class="item" style="left:243px;top:563px;width:230px"><b>Commercial and contract management of SCF3 contract.</b><br>Denholm Engineering Services Ltd<br>2018</p>
  <p class="item justify" style="left:243px;top:603px;width:230px"><b>Commercial management prior to adjudication, preparation of loss and/ or expense claim; assisted with drafting the Referral and subsequent adjudication documents, attended hearing and assisted with representation of the Client.</b><br>Brookvale Ltd<br>2017</p>
</section>

<section class="page page--two">
  <div class="header">
    <div class="portrait" role="img" aria-label="Portrait photo of the consultant in a dark pinstripe suit"></div>
    <h1 class="name">CALUM J MORAY</h1>
  </div>
  <p class="tagline">Construction Law, Disputes and Quantity Surveying Specialist</p>

  <h2 class="pill col-left" style="top:158px">CONTACT</h2>
  <div class="contact-row" style="top:190px">
    <svg width="9" height="9" viewBox="0 0 10 10"><path d="M2 1l2 2-1 1.3c.6 1.3 1.5 2.2 2.7 2.7L7 6l2 2-1.3 1.3C4.5 9 1 5.5.7 2.3z" fill="none" stroke="#276b7a" stroke-width=".8"/></svg>
    <span>+44 (0)7000 123 456</span></div>
  <div class="contact-row" style="top:206px">
    <svg width="9" height="9" viewBox="0 0 10 10"><rect x=".5" y="2" width="9" height="6" fill="none" stroke="#276b7a" stroke-width=".8"/><path d="M.5 2l4.5 3.5L9.5 2" fill="none" stroke="#276b7a" stroke-width=".8"/></svg>
    <span>calum@cjmqs.example</span></div>
  <div class="contact-row" style="top:222px">
    <svg width="9" height="11" viewBox="0 0 10 12"><path d="M5 11C2 7 1.5 5.5 1.5 4.5a3.5 3.5 0 017 0C8.5 5.5 8 7 5 11z" fill="none" stroke="#276b7a" stroke-width=".8"/><circle cx="5" cy="4.5" r="1.3" fill="none" stroke="#276b7a" stroke-width=".8"/></svg>
    <span>2nd Floor, 15 Harrow Crescent, Glasgow,</span></div>
  <div class="contact-row" style="top:238px"><span style="left:18px">Scotland, United Kingdom, G1 0AA</span></div>

  <h2 class="pill col-left" style="top:271px">EMPLOYMENT HISTORY</h2>
  <p class="item" style="left:32px;top:300px;width:165px"><b>Director of CJMQS Ltd</b><br>December 2018 to current</p>
  <p class="item" style="left:32px;top:334px;width:165px"><b>Ashby and Lowe Ltd (Contract &amp; Dispute Consultant)</b><br>January 2017 to November 2018</p>
  <p class="item" style="left:32px;top:389px;width:165px"><b>Fenwick Building Projects Ltd (Senior Quantity Surveyor)</b><br>November 2015 to December 2016</p>
  <p class="item" style="left:32px;top:437px;width:165px"><b>Birchfield Retirement Lifestyles Ltd</b><br>May 2015 to November 2015</p>
  <p class="item" style="left:32px;top:476px;width:165px"><b>DKR (Glasgow) Ltd – Contract Surveyor</b><br>February 2014 to May 2015</p>
  <p class="item" style="left:32px;top:516px;width:165px"><b>Marsh &amp; Findlay Ltd – Quantity Surveyor</b><br>February 2013 to February 2014</p>
  <p class="item" style="left:32px;top:555px;width:165px"><b>Marsh &amp; Findlay Ltd – Quantity Surveyor</b><br>February 2013 to February 2014</p>
  <p class="item" style="left:32px;top:594px;width:165px"><b>Oakridge (Glasgow) Ltd – Quantity Surveyor</b><br>March 2012 to February 2013</p>
  <p class="item" style="left:32px;top:636px;width:150px"><b>Linford Group (Hale &amp; Brown) – Cost Consultant</b><br>July 2006 to March 2012</p>

  <h2 class="pill col-right" style="top:158px">EXPERIENCE</h2>
  <p class="item justify" style="left:241px;top:187px;width:232px"><b>Commercial and contract management; preparation of claim for damages due to wrongful termination of building contract, assisted Harrow Beck with the quantum calculations and support during the adjudication and assisted with the drafting and reviewing of adjudication submissions.</b><br>Fenwick Building Projects Ltd<br>2016</p>

  <h2 class="pill col-right" style="top:282px">TRAINING AND COURSES</h2>
  <p class="item" style="left:241px;top:311px;width:145px">The Royal Institute of Building Surveyors, APC Assessor Training</p>
  <p class="date" style="left:413px;top:311px">October 2021</p>
  <p class="item" style="left:241px;top:342px;width:120px">The Institute of Dispute Arbitrators<br>Diploma in International Arbitration<br>(Module 1)</p>
  <p class="date" style="left:413px;top:342px">October 2021</p>
  <p class="item" style="left:241px;top:395px;width:145px">The Royal Institute of Building Surveyors; APC Counsellor Training</p>
  <p class="date" style="left:413px;top:395px">December 2019</p>
  <p class="item" style="left:241px;top:426px;width:130px">The Institute of Dispute Arbitrators<br>Construction Adjudication Pathway<br>Module 1 – Law of Obligations and Civil Evidence<br>Module 2 – Construction Adjudication<br>Module 3 – Construction Adjudication<br>Module 4 – Decision Writing</p>
  <p class="date" style="left:413px;top:426px">2017 to 2019</p>
  <p class="item" style="left:241px;top:546px;width:150px">The University of Lowmoor<br>Masters of Law, Construction Law (with Merit)<br>Legal Research<br>Law of the Construction Industry<br>Law and Practice of Construction Management<br>Legal Process and the Law of Contracts and Other Obligations<br>Dispute Resolution<br>Arbitration Law</p>
  <p class="date" style="left:413px;top:546px">2017 to 2019</p>
</section>

</body>
</html>
```